Training Consultant for Oil and Gas Drillers needs logo for business cards

I teach oil and gas professionals the skills required to keep rigs from blowing up. The company name is "Night Shift Bore Safety", which is pronounced Nite Shiffed. Tour refers to the time on an oil rig when a worker is off for sleep and rest. I teach something called Well Control, which is how to maintain a pressure balance in the well so the hydro carbons don't come to surface unexpectedly( like the Grey Tide Platform).

Target Market(s)

Rig hands and oil companies

Contact Information for Business Card

Night Shift BS ( company name) with a new logo
My name (Derek Holloway )and Title (Well Control Consultant)
Phone number and address

Font styles to use
Serif
Sans Serif

Colors

Designer to choose colors to be used in the design.

Requirements
Must have
• I need a logo for the company. I do not have anything yet

```html
<!DOCTYPE html>
<html lang="en">
<head>
<meta charset="utf-8">
<title>Night Shift BS — Business Card</title>
<link rel="stylesheet" href="https://fonts.googleapis.com/css2?family=Montserrat:wght@700&family=Work+Sans:wght@400;500&display=swap">
<style>
  :root {
    --navy: #0f3560;
    --navy-deep: #0b2a4d;
    --sky: #2391d0;
    --paper: #ffffff;
    --paper-shade: #eef0f2;
    --ink: #1a2a3c;
    --backdrop: #3a3d42;
  }
  * { margin: 0; padding: 0; box-sizing: border-box; }
  html, body { width: 1200px; height: 900px; overflow: hidden; }
  body {
    background: var(--backdrop);
    display: flex; align-items: center; justify-content: center;
    font-family: "Work Sans", Arial, sans-serif;
  }
  .card {
    position: relative;
    width: 1050px; height: 600px;
    border-radius: 26px;
    overflow: hidden;
    background: linear-gradient(160deg, var(--paper-shade) 0%, var(--paper) 45%, var(--paper) 100%);
  }
  .card__waves { position: absolute; inset: 0; width: 100%; height: 100%; }
  .brand {
    position: absolute; left: 70px; top: 100px;
    display: flex; flex-direction: column; align-items: center; gap: 20px;
    width: 420px;
  }
  .brand__dot {
    width: 120px; height: 120px; border-radius: 50%;
    background: var(--sky);
  }
  .brand__name {
    font-family: "Montserrat", Arial, sans-serif;
    font-weight: 700; font-size: 52px; color: var(--navy);
    letter-spacing: 0.5px; white-space: nowrap;
  }
  .divider {
    position: absolute; left: 545px; top: 110px;
    width: 3px; height: 250px; background: var(--navy);
  }
  .contact {
    position: absolute; left: 585px; top: 118px;
    color: var(--ink);
  }
  .contact__name {
    font-size: 32px; font-weight: 500; color: var(--sky);
    letter-spacing: 1px; text-transform: uppercase; line-height: 1.1;
  }
  .contact__title { font-size: 22px; margin-bottom: 14px; }
  .contact__line {
    font-size: 22px; line-height: 1.4;
    display: flex; align-items: center; gap: 10px;
  }
  .contact__line svg { width: 16px; height: 16px; flex: none; }
  .contact__accent { color: var(--sky); }
</style>
</head>
<body>
  <div class="card">
    <svg class="card__waves" viewBox="0 0 1050 600" preserveAspectRatio="none" aria-hidden="true">
      <path d="M0,378 Q330,505 1050,532 L1050,548 Q330,520 0,392 Z" fill="var(--sky)"/>
      <path d="M0,402 Q330,532 1050,560 L1050,600 L0,600 Z" fill="var(--navy)"/>
    </svg>

    <div class="brand">
      <div class="brand__dot"></div>
      <div class="brand__name">Night Shift BS</div>
    </div>

    <div class="divider"></div>

    <div class="contact">
      <div class="contact__name">Derek Holloway</div>
      <div class="contact__title">Well Control Consultant</div>
      <div class="contact__line">4182 Ridgeline Dr.</div>
      <div class="contact__line">Midland, TX 79705</div>
      <div class="contact__line">
        <svg viewBox="0 0 16 16"><path d="M4 1l3 3-2 2c1 2 3 4 5 5l2-2 3 3-2 3C7 15 1 9 1 3z" fill="var(--sky)"/></svg>
        1300 462 771
      </div>
      <div class="contact__line">
        <svg viewBox="0 0 16 16"><rect x="1" y="3" width="14" height="10" rx="1" fill="none" stroke="var(--sky)" stroke-width="1.6"/><path d="M1 4l7 5 7-5" fill="none" stroke="var(--sky)" stroke-width="1.6"/></svg>
        info@nightshiftbs.com
      </div>
      <div class="contact__line">
        <svg viewBox="0 0 16 16"><circle cx="8" cy="8" r="6.5" fill="none" stroke="var(--sky)" stroke-width="1.5"/><path d="M1.5 8h13M8 1.5c-3 3.5-3 9.5 0 13M8 1.5c3 3.5 3 9.5 0 13" fill="none" stroke="var(--sky)" stroke-width="1.2"/></svg>
        <span>www.<span class="contact__accent">nightshiftbs</span>.com</span>
      </div>
    </div>
  </div>
</body>
</html>
```